INNOVATIVE DESIGN NEEDED FOR FINANCIAL COMPANY

INTERNATIONAL FIRM IN HONG KONG NEEDS A MODERN BUSINESS CARD DESIGN. ONE SIDE ENGLISH OTHER SIDE IN CHINESE. WE ARE OPEN TO CHANGING FONTS AND COLOR. SHOULD BE A CARD THAT IS PROFESSIONAL DEALING WITH HIGH NET WORTH CLIENTELE. BOTH SIDES OF THE CARD WILL BE THE SAME, HOWEVER, THE WORDING ON ONE SIDE WILL BE ENGLISH AND THE OTHER SIDE IN CHINESE (CAN ASSIST IN THE LETTERING - CAN PROVIDE ONCE CARD DESIGN IS ACCEPTED.

Target Market(s)

Hong Kong/CHINA

Contact Information for Business Card

ATTRACTIVE MODERN

```html
<!DOCTYPE html>
<html lang="en">
<head>
<meta charset="utf-8">
<title>Linden Crest Capital – Business Card</title>
<link href="https://fonts.googleapis.com/css2?family=Roboto+Condensed:wght@400;700&family=Noto+Sans+TC:wght@400;700&display=swap" rel="stylesheet">
<style>
  :root {
    --brand-green: #14825a;
    --ink: #2b2b2b;
    --card-top: #f7f7f7;
    --card-bottom: #e9e9e9;
    --backdrop: #bdbdbd;
  }
  html, body {
    margin: 0; padding: 0;
    width: 1200px; height: 576px;
    overflow: hidden;
    background: var(--backdrop);
  }
  .canvas { position: relative; width: 1200px; height: 576px; }
  .card {
    position: absolute; top: 138px;
    width: 485px; height: 292px;
    border-radius: 11px; overflow: hidden;
    background: linear-gradient(160deg, var(--card-top), var(--card-bottom));
    font-family: "Roboto Condensed", "Noto Sans TC", sans-serif;
    color: var(--ink);
  }
  .card--english { left: 82px; }
  .card--chinese { left: 602px; font-family: "Noto Sans TC", "Roboto Condensed", sans-serif; }
  .card__band {
    position: absolute; left: 0; right: 0; bottom: 0; height: 12px;
    background: var(--brand-green);
  }
  .brand-mark {
    position: absolute; left: 29px; top: 34px;
    display: flex; align-items: center; gap: 7px;
  }
  .brand-mark__dot {
    width: 26px; height: 26px; border-radius: 50%;
    background: var(--brand-green);
  }
  .brand-mark__name {
    font-family: "Roboto Condensed", sans-serif;
    font-weight: 700; font-size: 15px; color: var(--brand-green);
  }
  .company {
    position: absolute; right: 31px; top: 35px; text-align: right;
  }
  .company__zh {
    font-family: "Noto Sans TC", sans-serif;
    font-weight: 700; font-size: 19px; line-height: 22px; letter-spacing: 0.5px;
  }
  .company__en {
    font-family: "Roboto Condensed", sans-serif;
    font-weight: 700; font-size: 14px; line-height: 17px;
  }
  .person { position: absolute; left: 30px; right: 31px; top: 151px; }
  .person__name {
    font-weight: 700; font-size: 22px; line-height: 26px; color: var(--brand-green);
  }
  .card--chinese .person__name { font-size: 21px; letter-spacing: 1px; }
  .person__role {
    display: flex; align-items: flex-end; gap: 4px;
    font-size: 11px; line-height: 14px;
  }
  .person__rule { flex: 1; height: 1px; background: var(--brand-green); margin-bottom: 3px; }
  .card--chinese .person__rule { flex: none; width: 331px; margin-left: auto; }
  .contacts {
    position: absolute; left: 30px; top: 213px;
    list-style: none; margin: 0; padding: 0;
    font-size: 12px; line-height: 17.5px;
  }
  .card--chinese .contacts { font-size: 12.5px; }
  .contacts li { display: flex; align-items: center; gap: 12px; }
  .contacts svg { width: 12px; height: 12px; fill: var(--brand-green); flex: none; }
  .address {
    position: absolute; right: 31px; top: 230px; text-align: right;
    font-size: 12px; line-height: 17.5px;
  }
</style>
</head>
<body>
<div class="canvas">

  <section class="card card--english" lang="en">
    <div class="brand-mark"><span class="brand-mark__dot"></span><span class="brand-mark__name">Linden Crest</span></div>
    <header class="company">
      <div class="company__zh" lang="zh-Hant">林峰資本有限公司</div>
      <div class="company__en">Linden Crest Capital Ltd</div>
    </header>
    <div class="person">
      <div class="person__name">CHAN Oliver</div>
      <div class="person__role"><span>Responsible Officer</span><span class="person__rule"></span></div>
    </div>
    <ul class="contacts">
      <li><svg viewBox="0 0 12 12"><path d="M1 4c0-2 2-3 5-3s5 1 5 3v1H8.5V3.8h-5V5H1z M3 6h6l1.5 5h-9z"/></svg>852-555-0142</li>
      <li><svg viewBox="0 0 12 12"><path d="M0 2h12v8H0z M1 3l5 3.5L11 3" stroke="#f2f2f2" stroke-width="1"/></svg>oliver.chan@lindencrestcapital.com</li>
      <li><svg viewBox="0 0 12 12"><circle cx="6" cy="6" r="5.5"/><path d="M0.5 6h11 M6 0.5v11 M6 0.5c-3 3-3 8 0 11 M6 0.5c3 3 3 8 0 11" stroke="#f2f2f2" stroke-width="0.8" fill="none"/></svg>www.lindencrestcapital.com</li>
    </ul>
    <address class="address" style="font-style:normal">18 Harbour Road,<br>Wan Chai, Hong Kong 000852</address>
    <div class="card__band"></div>
  </section>

  <section class="card card--chinese" lang="zh-Hant">
    <div class="brand-mark"><span class="brand-mark__dot"></span><span class="brand-mark__name">Linden Crest</span></div>
    <header class="company">
      <div class="company__zh">林峰資本有限公司</div>
      <div class="company__en" lang="en">Linden Crest Capital Ltd</div>
    </header>
    <div class="person">
      <div class="person__name">陳立文</div>
      <div class="person__role"><span>負責人員</span><span class="person__rule"></span></div>
    </div>
    <ul class="contacts">
      <li><svg viewBox="0 0 12 12"><path d="M1 4c0-2 2-3 5-3s5 1 5 3v1H8.5V3.8h-5V5H1z M3 6h6l1.5 5h-9z"/></svg>852-555-0142</li>
      <li><svg viewBox="0 0 12 12"><path d="M0 2h12v8H0z M1 3l5 3.5L11 3" stroke="#f2f2f2" stroke-width="1"/></svg>陳立文@林峰資本有限公司.com</li>
      <li><svg viewBox="0 0 12 12"><circle cx="6" cy="6" r="5.5"/><path d="M0.5 6h11 M6 0.5v11 M6 0.5c-3 3-3 8 0 11 M6 0.5c3 3 3 8 0 11" stroke="#f2f2f2" stroke-width="0.8" fill="none"/></svg>www.林峰資本有限公司.com</li>
    </ul>
    <address class="address" style="font-style:normal">港灣道18號,<br>灣仔區, 香港 000852</address>
    <div class="card__band"></div>
  </section>

</div>
</body>
</html>
```